DL Flyer for vehicle buying/selling service and advice business

New business to help people sell their current vehicle then select and buy and maintain their next car. (New or used).
We'll prepare and sell your car for you and get $,000s more than a trade in.
Offer advice as to the best car currently on the market based on our customer's needs.
With country wide sourcing network of cars across all manufacturers we have great buying power to ensure the very best possible price.
Personal service, including preparation of car for sale, pickup of old and drop-off of new vehicles, organise RWC and any required repairs.
We are NOT a car dealer so we WILL not try to sell you the vehicles we own.
Totally impartial, professional and friendly service making the purchase of your next car a great experience.

Flyer wording===========“Don’t sell your car or buy your next car without speaking to us”We guarantee to get you a better price for your current car and to find a cheaper purchase price for your next car.With a country wide sourcing network of cars “new and used” across all manufacturers we have sensational buying power to ensure the very best possible price.We can source the right car on any budget, from $2,000 to $200,000We are NOT a car dealer so we WILL not try to sell you the vehicles we own.By not being affiliated with any individual car manufacturer or dealer we can offer absolute impartiality.We’ll sit with you to discuss the best car for your needs and even bring the car to you for a test drive without the pressure of a salesperson nearby.Our services include:• Selling your current car: - Obtaining a roadworthy certificate - Organising any repairs needed - Detailing your car (wash, vacuum, polish) - Advertising of your car - Dealing with potential buyers - Negotiating the best price on your behalf• Assisting with the selection of your next car• Organising test drives• Purchasing the car of your choice - Sourcing the very best price• Ongoing management of their vehicle (service, clean, repair)Possible inclusions in the flyer might be:Advantages of upgrading to a new vehicle include:o reliability, o safety,o fuel efficiencyo comfort.Space for a couple of short testimonials Background images of all of the major car manufacturers Added Friday, July 29, 2016

Target Market(s)

Local community.
Initially will drop DL flyers in local post boxes

Industry/Entity Type

Business

Requirements
Must have
• Flyer wording:
• ===========
• “Don’t sell your car or buy your next car without speaking to us”
• ---------------------------------------------------------------------------------
• We guarantee to get you a better price for your current car and to find a cheaper purchase price for your next car.
• With a country wide sourcing network of cars “new and used” across all manufacturers we have sensational buying power to ensure the very best possible price.
• We can source the right car on any budget, from $2,000 to $200,000
• We are NOT a car dealer so we WILL not try to sell you the vehicles we own.
• By not being affiliated with any individual car manufacturer or dealer we can offer absolute impartiality.
• We’ll sit with you to discuss the best car for your needs and even bring the car to you for a test drive without the pressure of a salesperson nearby.
• Our services include:
• • Selling your current car:
• o Obtaining a roadworthy certificate
• o Organising any repairs needed
• o Detailing your car (wash, vacuum, polish)
• o Advertising of your car
• o Dealing with potential buyers
• o Negotiating the best price on your behalf
• • Assisting with the selection of your next car
• • Organising test drives
• • Purchasing the car of your choice
• o Sourcing the very best price
• • Ongoing management of your vehicle (service, clean, repair)
• Call Gregor on: 0438 215064
Nice to have
• Possible inclusions on the flyer might be:
• List of advantages of upgrading to a new vehicle:
• o reliability,
• o safety,
• o fuel efficiency
• o comfort
• Space for a couple of short testimonials
• Background images of all of the major car manufacturers

```html
<!DOCTYPE html>
<html lang="en">
<head>
<meta charset="utf-8">
<title>Keystone Car Advisors – DL Flyer</title>
<link rel="stylesheet" href="https://fonts.googleapis.com/css2?family=Oswald:wght@500;600&family=Lato:wght@400;700&display=swap">
<style>
  :root {
    --red: #e3141c;
    --red-dark: #8e0a0e;
    --ink: #1c1c1c;
    --paper: #f4f4f5;
    --paper-edge: #d9dadc;
    --silver-light: #f2f2f2;
    --silver-dark: #8a8c90;
    --photo-top: #5b6470;
    --photo-bottom: #2a2c30;
    --rule: #b9babd;
  }
  * { margin: 0; padding: 0; box-sizing: border-box; }
  html, body { width: 1200px; height: 2469px; overflow: hidden; background: #ffffff; }
  .flyer {
    position: relative;
    width: 1200px;
    height: 2469px;
    overflow: hidden;
    background: radial-gradient(ellipse at 50% 45%, #ffffff 0%, var(--paper) 45%, var(--paper-edge) 100%);
    font-family: "Lato", Arial, sans-serif;
    color: var(--ink);
  }
  .flyer__art { position: absolute; inset: 0; width: 1200px; height: 2469px; }
  .brand {
    position: absolute;
    left: 78px; top: 360px;
    width: 300px; height: 300px;
    background: #ffffff;
    display: flex; align-items: center; justify-content: center;
    text-align: center;
    box-shadow: 0 6px 18px rgba(0,0,0,.25);
  }
  .brand__name {
    font-family: "Oswald", Arial, sans-serif;
    font-weight: 600;
    font-size: 58px;
    line-height: 1.05;
    color: var(--red);
    text-transform: uppercase;
  }
  .headline {
    position: absolute;
    left: 98px; top: 766px;
    width: 1009px; height: 243px;
    border-radius: 56px;
    border: 6px solid #2a0506;
    background: linear-gradient(180deg, #f0343a 0%, var(--red) 38%, #b80d13 62%, var(--red-dark) 100%);
    box-shadow: 0 10px 22px rgba(0,0,0,.35), inset 0 4px 0 rgba(255,255,255,.25);
    color: #ffffff;
    text-align: center;
    font-family: "Oswald", Arial, sans-serif;
    font-weight: 600;
    text-transform: uppercase;
    display: flex; flex-direction: column; justify-content: center;
    text-shadow: 0 2px 3px rgba(0,0,0,.35);
  }
  .headline__lead { font-size: 50px; line-height: 1.1; letter-spacing: -0.5px; }
  .headline__main { font-size: 74px; line-height: 1.1; font-weight: 500; letter-spacing: 1px; }
  .pitch {
    position: absolute;
    left: 130px; top: 1070px;
    width: 968px;
    font-size: 34.5px;
    line-height: 44px;
  }
  .pitch__point { padding: 12px 0 16px; }
  .pitch__point + .pitch__point { border-top: 3px solid var(--rule); }
  .accent { color: var(--red); font-weight: 700; }
</style>
</head>
<body>
<main class="flyer">
  <svg class="flyer__art" viewBox="0 0 1200 2469" aria-hidden="false">
    <defs>
      <linearGradient id="silver" x1="0" y1="0" x2="1" y2="0">
        <stop offset="0" stop-color="var(--silver-light)"/>
        <stop offset="0.55" stop-color="#c4c5c8"/>
        <stop offset="1" stop-color="var(--silver-dark)"/>
      </linearGradient>
      <linearGradient id="topPhoto" x1="0" y1="0" x2="1" y2="1">
        <stop offset="0" stop-color="#8a96a6"/>
        <stop offset="0.5" stop-color="var(--photo-top)"/>
        <stop offset="1" stop-color="#1d2128"/>
      </linearGradient>
      <linearGradient id="bottomPhoto" x1="0" y1="0" x2="1" y2="1">
        <stop offset="0" stop-color="#6d5a4a"/>
        <stop offset="0.45" stop-color="var(--photo-bottom)"/>
        <stop offset="1" stop-color="#121316"/>
      </linearGradient>
      <linearGradient id="redTri" x1="0" y1="0" x2="1" y2="0">
        <stop offset="0" stop-color="#ff2a30"/>
        <stop offset="1" stop-color="#c40d13"/>
      </linearGradient>
    </defs>

    <polygon class="photo photo--top" role="img" aria-label="Photo: two smiling women at an open car door, one holding up the keys"
             points="0,0 1200,0 1200,630 0,450" fill="url(#topPhoto)"/>
    <polygon class="band band--silver" points="441,520 1200,680 1200,727 441,560" fill="url(#silver)"/>
    <polygon class="band band--shade" points="0,450 441,520 441,560 0,490" fill="#ffffff" opacity=".6"/>

    <polygon class="band band--silver" points="0,1855 1200,2300 1200,2345 0,1895" fill="url(#silver)"/>
    <polygon class="photo photo--bottom" role="img" aria-label="Photo: a delighted young woman holding up new car keys beside a dark car"
             points="0,1895 1200,2345 1200,2469 0,2469" fill="url(#bottomPhoto)"/>
    <polygon class="photo photo--bottom" role="img" aria-label="Photo continues: dark car door behind the woman"
             points="0,1855 0,1895 1200,2345 1200,2300" fill="none"/>
    <polygon class="band band--silver" points="700,2110 1200,1840 1200,1883 759,2095" fill="url(#silver)"/>
    <polygon class="accent-triangle" points="759,2095 1200,1883 1200,2222" fill="url(#redTri)"/>
  </svg>

  <div class="brand">
    <span class="brand__name">Keystone<br>Car<br>Advisors</span>
  </div>

  <h1 class="headline">
    <span class="headline__lead">Don’t sell your car or buy your next car</span>
    <span class="headline__main">Without speaking to us</span>
  </h1>

  <section class="pitch">
    <p class="pitch__point">We guarantee to get you a better price for your current car and to find a cheaper purchase price for your next car.</p>
    <p class="pitch__point">With a country wide sourcing network of cars <span class="accent">“new and used”</span> across all manufacturers we have sensational buying power to ensure the very best possible price.</p>
    <p class="pitch__point">We can source the right car on any budget, from <span class="accent">$2,000 to $200,000</span></p>
    <p class="pitch__point">We are NOT a car dealer so we WILL not try to sell you the vehicles we own.</p>
    <p class="pitch__point">By not being affiliated with any individual car manufacturer or dealer we can offer absolute impartiality.</p>
    <p class="pitch__point">We’ll sit with you to discuss the best car for your needs and even bring the car to you for a test drive without the pressure of a salesperson nearby.</p>
  </section>
</main>
</body>
</html>
```